Criação de Logo e Papelaria (6 itens) para TREINAMENTO EM GESTAO
A empresa queria:
" É uma empresa que faz treinamentos de gestao, liderança, gestao em geral para empresários, funcionários e parceiros de negócio. "

```html
<!DOCTYPE html>
<html lang="pt-BR">
<head>
<meta charset="utf-8">
<title>Lumena Training — Pasta institucional</title>
<link rel="stylesheet" href="https://fonts.googleapis.com/css2?family=Cinzel:wght@400&display=swap">
<style>
  :root {
    --teal-deep: #0f7c93;
    --teal-mid: #2fa3b6;
    --teal-light: #6cc7d3;
    --teal-ink: #2a93a8;
    --paper: #ffffff;
    --dieline: #c9d3d6;
    --canvas: #ffffff;
  }
  html, body {
    margin: 0;
    padding: 0;
    width: 1200px;
    height: 1200px;
    overflow: hidden;
    background: var(--canvas);
  }
  .folder {
    display: block;
    width: 1200px;
    height: 1200px;
  }
  .brand-text {
    font-family: "Cinzel", "Times New Roman", serif;
    font-weight: 400;
  }
  .contact-line {
    font-family: "Cinzel", "Times New Roman", serif;
    font-size: 15px;
    letter-spacing: 2.4px;
    fill: var(--paper);
  }
  .pocket-line {
    font-family: "Cinzel", "Times New Roman", serif;
    font-size: 9px;
    letter-spacing: 0.8px;
    fill: var(--paper);
  }
  .cover-name {
    fill: var(--teal-ink);
    font-size: 84px;
    letter-spacing: 4px;
  }
  .cover-tagline {
    fill: var(--teal-ink);
    font-size: 26px;
    letter-spacing: 5px;
  }
</style>
</head>
<body>
<svg class="folder" viewBox="0 0 1200 1200" xmlns="http://www.w3.org/2000/svg">
  <defs>
    <linearGradient id="back-panel-fill" x1="0" y1="0" x2="1" y2="0">
      <stop offset="0" stop-color="var(--teal-deep)"/>
      <stop offset="0.55" stop-color="var(--teal-mid)"/>
      <stop offset="1" stop-color="var(--teal-light)"/>
    </linearGradient>
    <linearGradient id="pocket-swoosh-fill" x1="0" y1="0" x2="1" y2="0">
      <stop offset="0" stop-color="var(--teal-light)" stop-opacity="0.2"/>
      <stop offset="0.5" stop-color="var(--teal-mid)"/>
      <stop offset="1" stop-color="var(--teal-deep)"/>
    </linearGradient>
    <linearGradient id="artwork-fill" x1="0" y1="0" x2="1" y2="1">
      <stop offset="0" stop-color="#ffffff" stop-opacity="0.22"/>
      <stop offset="1" stop-color="#ffffff" stop-opacity="0.08"/>
    </linearGradient>
  </defs>

  <!-- glue tab on the left edge -->
  <path class="glue-tab" d="M122 650 L78 672 L78 820 L122 842 Z" fill="var(--paper)" stroke="var(--dieline)" stroke-width="1.5"/>
  <path class="glue-tab-slot" d="M86 700 Q104 706 110 726" fill="none" stroke="var(--dieline)" stroke-width="1.5"/>

  <!-- back panel -->
  <g class="back-panel">
    <rect x="122" y="53" width="508" height="740" fill="url(#back-panel-fill)"/>
    <g role="img" aria-label="Ilustração de três borboletas em traço branco voando da esquerda para a direita">
      <path d="M135 210 C200 200 290 250 330 330 C360 400 330 470 250 470 C190 470 140 430 135 380 Z" fill="url(#artwork-fill)"/>
      <ellipse cx="480" cy="320" rx="48" ry="44" fill="url(#artwork-fill)"/>
      <ellipse cx="560" cy="245" rx="36" ry="38" fill="url(#artwork-fill)"/>
    </g>
    <g class="contact-block" text-anchor="middle">
      <text class="contact-line" x="376" y="762">RUA DAS ACÁCIAS Nº 512 | 3º ANDAR | SALA 210</text>
      <text class="contact-line" x="376" y="784">BOTAFOGO | RIO DE JANEIRO | 22041000</text>
      <text class="contact-line" x="376" y="806">CONTATO@LUMENA.COM.BR</text>
      <text class="contact-line" x="376" y="828">WWW.LUMENA.COM.BR</text>
    </g>
  </g>

  <!-- inner pocket flap below the back panel -->
  <g class="pocket-flap">
    <path d="M144 793 L610 793 L590 1130 L160 1130 Z" fill="var(--paper)" stroke="var(--dieline)" stroke-width="1.5"/>
    <path d="M144 793 L610 793 L604 900 C520 850 430 900 330 940 C250 970 190 960 150 930 Z" fill="url(#back-panel-fill)"/>
    <path class="pocket-slit-tab" d="M600 960 L620 980 L614 1110 L594 1120" fill="var(--paper)" stroke="var(--dieline)" stroke-width="1.5"/>
    <g class="pocket-brand" transform="rotate(180 490 985)" text-anchor="middle">
      <circle cx="490" cy="958" r="8" fill="var(--teal-ink)"/>
      <text class="brand-text" x="490" y="994" font-size="26" letter-spacing="2" fill="var(--teal-ink)">LUMENA</text>
      <text class="brand-text" x="490" y="1010" font-size="9" letter-spacing="2" fill="var(--teal-ink)">TRAINING</text>
    </g>
  </g>

  <!-- front cover -->
  <g class="front-cover">
    <rect x="630" y="53" width="518" height="740" fill="var(--paper)"/>
    <path d="M630 793 L1148 793 L1148 53" fill="none" stroke="var(--dieline)" stroke-width="1"/>
    <g class="cover-brand" text-anchor="middle">
      <circle cx="888" cy="400" r="12" fill="var(--teal-ink)"/>
      <text class="brand-text cover-name" x="888" y="522">LUMENA</text>
      <line x1="728" y1="563" x2="788" y2="563" stroke="var(--teal-ink)" stroke-width="1.5"/>
      <line x1="988" y1="563" x2="1048" y2="563" stroke="var(--teal-ink)" stroke-width="1.5"/>
      <text class="brand-text cover-tagline" x="888" y="573">TRAINING</text>
    </g>
    <path class="cover-swoosh" d="M630 858 C780 850 980 810 1148 712 L1148 868 C1000 892 820 880 630 858 Z" fill="url(#pocket-swoosh-fill)"/>
    <g class="cover-contact" text-anchor="end">
      <text class="pocket-line" x="1128" y="790">LUMENA TRAINING</text>
      <text class="pocket-line" x="1128" y="803">21 3456-7890 | 21 98765-4321</text>
      <text class="pocket-line" x="1128" y="816">CONTATO@LUMENA.COM.BR</text>
      <text class="pocket-line" x="1128" y="829">WWW.LUMENA.COM.BR</text>
    </g>
  </g>
</svg>
</body>
</html>
```